Box Package Design for Voratel Self Defense Keychain

Need a printable design for boxes. Something that will convey the message of "strength" and "self defense." Will upload the box types that will be used. As well as the logo (which will be revised by ArtFlockHub people) which will have some changes too it. I am still waiting on the new design. Color scheme is green or dark green. Also included are some photos of the actual product. The images serve as a guide only ... you can however your creative juices flow.

Target Market(s)

People in the self-defense niche

Industry/Entity Type

Defense

Font styles to use
Serif

Colors
aacf37
abd037
cadf82

Requirements
Must have
• No idea ...
Nice to have
• A circular design.
Should not have
• No idea ... I have 0 artistic inclinations

```html
<!DOCTYPE html>
<html lang="en">
<head>
<meta charset="utf-8">
<title>RKD Voratel – Box Lid Design</title>
<link rel="stylesheet" href="https://fonts.googleapis.com/css2?family=Orbitron:wght@500;800&display=swap">
<style>
  :root {
    --page-bg: #d8d8d8;
    --lid-green-light: #9fdca0;
    --lid-green-mid: #5cc266;
    --lid-green-deep: #2f9a3a;
    --band-black: #0c0c0c;
    --band-edge: #1f1f1f;
    --title-black: #111111;
    --brand-green: #3aa646;
    --product-dark: #1b1b1b;
    --product-glow: rgba(200, 240, 200, 0.35);
  }
  * { margin: 0; padding: 0; box-sizing: border-box; }
  html, body {
    width: 1200px;
    height: 1050px;
    overflow: hidden;
    background: var(--page-bg);
  }
  .canvas {
    position: relative;
    width: 1200px;
    height: 1050px;
    background: var(--page-bg);
    font-family: "Orbitron", sans-serif;
  }
  .box-lid {
    position: absolute;
    left: 110px;
    top: 110px;
    width: 980px;
    height: 560px;
    background:
      radial-gradient(ellipse at 35% 80%, var(--lid-green-light) 0%, transparent 60%),
      linear-gradient(160deg, var(--lid-green-mid) 0%, var(--lid-green-mid) 40%, var(--lid-green-deep) 100%);
  }
  .lid-title {
    position: absolute;
    left: 0;
    right: 0;
    top: 55px;
    text-align: center;
    color: var(--title-black);
    line-height: 1;
  }
  .lid-title .title-brand {
    display: block;
    font-weight: 800;
    font-size: 92px;
    letter-spacing: 6px;
  }
  .lid-title .title-product {
    display: block;
    margin-top: 18px;
    font-weight: 500;
    font-size: 118px;
    letter-spacing: 14px;
  }
  .product-photo {
    position: absolute;
    left: 74px;
    top: 320px;
    width: 820px;
    height: 170px;
    border-radius: 12px;
    background: linear-gradient(90deg, var(--product-dark) 0%, rgba(27, 27, 27, 0.75) 55%, var(--product-glow) 100%);
  }
  .box-front {
    position: absolute;
    left: 110px;
    top: 670px;
    width: 980px;
    height: 190px;
    background: linear-gradient(180deg, var(--band-edge) 0%, var(--band-black) 100%);
    display: flex;
    align-items: center;
    justify-content: center;
  }
  .brand-mark {
    display: flex;
    align-items: center;
    gap: 12px;
    color: var(--brand-green);
    font-weight: 800;
    letter-spacing: 3px;
    white-space: nowrap;
  }
  .brand-mark .mark-dot {
    width: 22px;
    height: 22px;
    border-radius: 50%;
    background: var(--brand-green);
  }
  .box-front .brand-mark { font-size: 30px; }
  .corner-mark {
    position: absolute;
    right: 60px;
    bottom: 60px;
    font-size: 34px;
  }
</style>
</head>
<body>
  <main class="canvas">
    <section class="box-lid">
      <h1 class="lid-title">
        <span class="title-brand">RKD</span>
        <span class="title-product">VORATEL</span>
      </h1>
      <div class="product-photo" role="img" aria-label="Product photograph: black ribbed self-defense keychain with a silver key ring"></div>
    </section>

    <section class="box-front">
      <div class="brand-mark">
        <span class="mark-dot"></span>
        <span class="mark-name">RKD VORATELS</span>
      </div>
    </section>

    <div class="brand-mark corner-mark">
      <span class="mark-dot"></span>
      <span class="mark-name">RKD VORATELS</span>
    </div>
  </main>
</body>
</html>
```